Wine Label Design

We are looking for a new label to add to our winery. This is to be named "Lindgrube" which is the German word for schoolhouse. Our tasting room is a one room school house built in 1887. I would like the label to be very simple and clean with a schoolhouse on the front. I would like to schoolhouse to be sketch style, not a cartoonish design. I have attached a photo of the schoolhouse that we pour from, this is what I would want the schoolhouse to resemble. I have also added a copy of our current "higher end" label so that you have an idea of our style. I would like the new label to be cohesive with our old label and look good next to each other on our shelves. Just as added clarification we do not want Harlen Vineyards on the new label - we want that replaced with Lindgrube. If you are unable to do a full label design we would also accept just the schoolhouse drawing design as well. Thank you.

Logo Text

Lindgrube

```html
<!DOCTYPE html>
<html lang="en">
<head>
<meta charset="utf-8">
<title>Lindgrube Dry Rosé Label</title>
<link rel="stylesheet" href="https://fonts.googleapis.com/css2?family=Cinzel:wght@400;600;700&family=Parisienne&display=swap">
<style>
  :root {
    --page-bg: #f3f3f3;
    --sheet-bg: #ffffff;
    --label-bg: #251e14;
    --label-text: #ffffff;
    --accent-gold: #e2aa2c;
    --mark-grey: #7a726a;
  }
  html, body {
    margin: 0;
    padding: 0;
    width: 1200px;
    height: 1000px;
    overflow: hidden;
    background: var(--page-bg);
  }
  .canvas {
    position: relative;
    width: 1200px;
    height: 1000px;
  }
  .sheet {
    position: absolute;
    left: 100px;
    top: 88px;
    width: 1000px;
    height: 833px;
    background: var(--sheet-bg);
  }
  .label-shape {
    position: absolute;
    left: 0;
    top: 0;
  }
  .label-badge {
    position: absolute;
    left: 582px;
    top: 240px;
    width: 28px;
    height: 28px;
    background: var(--accent-gold);
  }
  .label-text {
    position: absolute;
    left: 397px;
    width: 398px;
    margin: 0;
    text-align: center;
    color: var(--label-text);
    line-height: 1;
  }
  .label-title {
    top: 304px;
    font-family: "Cinzel", serif;
    font-weight: 600;
    font-size: 54px;
    letter-spacing: 1px;
  }
  .label-vintage {
    top: 438px;
    font-family: "Cinzel", serif;
    font-weight: 700;
    font-size: 15px;
    letter-spacing: 3px;
  }
  .label-variety {
    top: 488px;
    font-family: "Parisienne", cursive;
    font-size: 40px;
  }
  .label-region {
    top: 577px;
    font-family: "Cinzel", serif;
    font-size: 16px;
    letter-spacing: 0.5px;
  }
  .brand-mark {
    position: absolute;
    left: 0;
    width: 1200px;
    top: 738px;
    margin: 0;
    text-align: center;
    font-family: "Cinzel", serif;
    font-weight: 700;
    font-size: 56px;
    line-height: 1;
    color: var(--mark-grey);
  }
</style>
</head>
<body>
  <div class="canvas">
    <div class="sheet"></div>

    <svg class="label-shape" width="1200" height="1000" viewBox="0 0 1200 1000" aria-hidden="true">
      <path d="M397 218 Q596 146 795 218 L795 643 L397 643 Z" fill="var(--label-bg)"/>
    </svg>

    <div class="label-badge" aria-hidden="true"></div>
    <h1 class="label-text label-title">Lindgrube</h1>
    <p class="label-text label-vintage">2016</p>
    <p class="label-text label-variety">Dry Rose</p>
    <p class="label-text label-region">Finger Lakes</p>

    <p class="brand-mark">Lindgrube</p>
  </div>
</body>
</html>
```